label design for oral care product

Kindly invite you to design bottle label (114 mm*40 mm) for our product, a kind of oral care product. The GEL is different from our previous cleanser product, as the pic we uploaded for demonstration. The color of frosted glass bottle is dark green, but the cap is white. You could download the pic of bottle among the uploaded files. The logo file and label content description are attached too. Please check them. Our product is made from many kinds of natural plant extracts, which includes herb and fruit. I wish the label would make our product look high-end and reliable. And it would be better if you could give some advice on paper material and special requirements for printing, related to your design. I value the texture of label too, because I think that stands for the quality of products. No color limitation for the use of our logo.
20-40 female, who value oral health.

```html
<!DOCTYPE html>
<html lang="en">
<head>
<meta charset="utf-8">
<title>Aligner Gel – Bottle Label</title>
<link rel="stylesheet" href="https://fonts.googleapis.com/css2?family=Bebas+Neue&family=Maven+Pro:wght@400;600&display=swap">
<style>
  :root {
    --backdrop: #d9dcdc;
    --label-green: #2c3010;
    --label-green-deep: #1f230b;
    --ink-white: #ffffff;
    --ink-soft: #eef0e6;
  }
  * { margin: 0; padding: 0; box-sizing: border-box; }
  html, body {
    width: 1200px;
    height: 1100px;
    overflow: hidden;
    background: var(--backdrop);
  }
  .canvas {
    width: 1200px;
    height: 1100px;
    display: flex;
    align-items: center;
    justify-content: center;
  }
  .label {
    width: 1140px;
    height: 400px;
    background: radial-gradient(ellipse at 50% 35%, var(--label-green) 0%, var(--label-green-deep) 100%);
    color: var(--ink-white);
    display: flex;
    flex-direction: column;
    align-items: center;
    justify-content: center;
    text-align: center;
  }
  .brand {
    display: flex;
    align-items: center;
    gap: 8px;
    font-family: "Maven Pro", sans-serif;
    font-weight: 600;
    font-size: 30px;
    letter-spacing: 0.5px;
    text-transform: lowercase;
    margin-bottom: 30px;
  }
  .brand-dot {
    width: 10px;
    height: 10px;
    border-radius: 50%;
    background: var(--ink-white);
  }
  .product-name {
    font-family: "Bebas Neue", sans-serif;
    font-size: 76px;
    line-height: 1;
    letter-spacing: 6px;
  }
  .tagline {
    font-family: "Maven Pro", sans-serif;
    font-size: 15px;
    letter-spacing: 1px;
    margin-top: 8px;
    color: var(--ink-soft);
  }
  .benefits {
    font-family: "Maven Pro", sans-serif;
    font-size: 21px;
    line-height: 1.3;
    letter-spacing: 1px;
    margin-top: 42px;
  }
  .volume {
    font-family: "Maven Pro", sans-serif;
    font-size: 16px;
    letter-spacing: 1px;
    margin-top: 22px;
    color: var(--ink-soft);
  }
</style>
</head>
<body>
  <main class="canvas">
    <section class="label">
      <div class="brand"><span class="brand-name">Lumo Leaf</span><span class="brand-dot"></span></div>
      <h1 class="product-name">ALIGNER GEL</h1>
      <p class="tagline">IMMUNE SUPPORT FOR ORAL HEALTH</p>
      <p class="benefits">MAINTAIN DENTAL HYGIENE<br>&amp; STRENGTHEN GUMS</p>
      <p class="volume">30 ML / 1FL OZ</p>
    </section>
  </main>
</body>
</html>
```